Tallivo Limited Business Card

We need a business card for a new company based in Essex, United Kingdom. We develop and manufacture educational games. The business card needs to match the company brand and logo and the colour scheme.
My company makes educational board games to be played by the family or used by teachers
The games are tile based number game

Target Market(s)

Parents, teachers, schools and children

Industry/Entity Type

Games

Contact Information for Business Card

Company Name - Tallivo Limited
Director - Martin Dobbs
Registered Office - 3 Birch Court, 241 Harwell Lane, Brennock, Eastmere, QX7 4TP
Phone Number - 07841 563 218
Email - Enquiries@Tallivo.example
Website - www.Tallivo.example
Company Number - 08471362

Font styles to use
Sans Serif

Colors
00a990
ffffff

Requirements
Must have
• Same colour scheme as the attachments - green and white
• Same font style for Tallivo
• Images of the number tiles similar to the attachments
• extra details
• The colour is Cyan - 82 Magenta - 24 Yellow - 44 Black - 2
• I have attached some of the font styles use on my website and alos my LOGO
Nice to have
• Image of the number "1" tag as seen on the website

```html
<!DOCTYPE html>
<html lang="en">
<head>
<meta charset="utf-8">
<title>Tallivo Limited – Business Card</title>
<link rel="stylesheet" href="https://fonts.googleapis.com/css2?family=Nunito:wght@400;600;800&display=swap">
<style>
  :root {
    --teal: #168587;
    --teal-dark: #0f6a6d;
    --teal-light: #1c9696;
    --white: #ffffff;
    --paper: #f4f5f5;
    --backdrop: #e3e5e4;
    --tile-light: #e6e3ec;
    --tile-mid: #c9c3d4;
    --text-on-teal: #d6eeee;
  }
  * { box-sizing: border-box; margin: 0; padding: 0; }
  html, body {
    width: 1200px; height: 800px; overflow: hidden;
    background: var(--backdrop);
    font-family: "Nunito", sans-serif;
  }
  .stage {
    position: relative; width: 1200px; height: 800px;
    display: flex; align-items: center; justify-content: center; gap: 40px;
  }
  .card {
    position: relative; width: 540px; height: 350px;
    border-radius: 4px; overflow: hidden;
    box-shadow: 0 10px 28px rgba(0,0,0,0.18);
  }

  /* Back of card */
  .card--back {
    background: linear-gradient(135deg, var(--teal-light) 0%, var(--teal) 45%, var(--teal-dark) 100%);
    color: var(--text-on-teal);
  }
  .card--back .brand { position: absolute; left: 44px; top: 92px; }
  .brand__name { font-weight: 800; line-height: 1; letter-spacing: -0.5px; }
  .card--back .brand__name { font-size: 34px; color: var(--text-on-teal); }
  .brand__tagline { font-weight: 600; text-transform: uppercase; letter-spacing: 0.6px; }
  .card--back .brand__tagline { font-size: 9.5px; margin-top: 3px; color: var(--text-on-teal); }

  .tiles {
    position: absolute; border-radius: 10px;
    background: linear-gradient(135deg, var(--tile-light), var(--tile-mid));
    opacity: 0.9;
  }
  .tiles--large { right: 26px; top: 18px; width: 170px; height: 300px; }
  .tiles--small { left: 24px; bottom: 26px; width: 150px; height: 92px; }

  .copyright {
    position: absolute; left: 200px; bottom: 28px;
    font-size: 12px; line-height: 1.45; letter-spacing: 0.3px;
  }

  /* Front of card */
  .card--front { background: linear-gradient(160deg, var(--white), var(--paper)); color: var(--teal); }
  .accent-tab {
    position: absolute; top: 0; right: 0; width: 100px; height: 10px;
    background: var(--teal);
  }
  .card--front .brand { position: absolute; left: 40px; top: 116px; }
  .card--front .brand__name { font-size: 44px; color: var(--teal); }
  .card--front .brand__tagline { font-size: 10.5px; margin-top: 2px; }

  .person { position: absolute; left: 40px; top: 188px; }
  .person__name { font-size: 27px; font-weight: 400; letter-spacing: 0.5px; text-transform: uppercase; line-height: 1.05; }
  .person__role { font-size: 11px; font-weight: 800; text-transform: uppercase; letter-spacing: 0.5px; }

  .contact { list-style: none; font-size: 12.5px; line-height: 1.35; }
  .contact li { display: flex; align-items: flex-start; gap: 9px; margin-bottom: 3px; }
  .contact svg { flex: none; width: 11px; height: 13px; margin-top: 2px; fill: var(--teal); }
  .contact--office { position: absolute; left: 40px; top: 258px; }
  .contact--online { position: absolute; left: 352px; top: 146px; }
</style>
</head>
<body>
<main class="stage">

  <section class="card card--back" aria-label="Business card, back">
    <div class="tiles tiles--large" role="img" aria-label="Stacked cluster of rounded number tiles with coloured rings and digits"></div>
    <div class="tiles tiles--small" role="img" aria-label="Small group of rounded number tiles with coloured rings and digits"></div>
    <div class="brand">
      <div class="brand__name">Tallivo</div>
      <div class="brand__tagline">Fast paced number games</div>
    </div>
    <p class="copyright">Copyright 2017 by<br>Tallivo Ltd.<br>All rights reserved.</p>
  </section>

  <section class="card card--front" aria-label="Business card, front">
    <div class="accent-tab"></div>
    <div class="brand">
      <div class="brand__name">Tallivo</div>
      <div class="brand__tagline">Fast paced number games</div>
    </div>
    <div class="person">
      <h1 class="person__name">Martin Dobbs</h1>
      <p class="person__role">Director</p>
    </div>
    <ul class="contact contact--office">
      <li>
        <svg viewBox="0 0 12 16" aria-hidden="true"><path d="M6 0a6 6 0 0 0-6 6c0 4.5 6 10 6 10s6-5.5 6-10a6 6 0 0 0-6-6zm0 8.5A2.5 2.5 0 1 1 6 3.5a2.5 2.5 0 0 1 0 5z"/></svg>
        <span>3 Birch Court, 241 Harwell Lane,<br>Brennock, Eastmere, QX7 4TP</span>
      </li>
      <li>
        <svg viewBox="0 0 10 16" aria-hidden="true"><path d="M1.5 0h7A1.5 1.5 0 0 1 10 1.5v13A1.5 1.5 0 0 1 8.5 16h-7A1.5 1.5 0 0 1 0 14.5v-13A1.5 1.5 0 0 1 1.5 0zM1.5 2v11h7V2zm3.5 11.6a.8.8 0 1 0 0 1.6.8.8 0 0 0 0-1.6z"/></svg>
        <span>07841 563 218</span>
      </li>
    </ul>
    <ul class="contact contact--online">
      <li>
        <svg viewBox="0 0 16 12" aria-hidden="true"><path d="M0 0h16v1.5L8 7 0 1.5zM0 3.3l8 5.5 8-5.5V12H0z"/></svg>
        <span>Enquiries@Tallivo.example</span>
      </li>
      <li>
        <svg viewBox="0 0 16 16" aria-hidden="true"><path d="M8 0a8 8 0 1 0 0 16A8 8 0 0 0 8 0zm5.9 7h-2.6a12 12 0 0 0-1-4.7A6 6 0 0 1 13.9 7zM8 2.1c.7.9 1.2 2.6 1.3 4.9H6.7C6.8 4.7 7.3 3 8 2.1zM5.7 2.3a12 12 0 0 0-1 4.7H2.1a6 6 0 0 1 3.6-4.7zM2.1 9h2.6a12 12 0 0 0 1 4.7A6 6 0 0 1 2.1 9zM8 13.9c-.7-.9-1.2-2.6-1.3-4.9h2.6c-.1 2.3-.6 4-1.3 4.9zm2.3-.2a12 12 0 0 0 1-4.7h2.6a6 6 0 0 1-3.6 4.7z"/></svg>
        <span>www.Tallivo.example</span>
      </li>
      <li>
        <svg viewBox="0 0 16 16" aria-hidden="true"><path d="M3.6 0l2.6 3.4-1.6 2.1c.9 2 2.8 3.9 4.9 4.9l2.1-1.6L16 12.4 13.9 16C6.5 15.4.6 9.5 0 2.1z"/></svg>
        <span>08471362</span>
      </li>
    </ul>
  </section>

</main>
</body>
</html>
```